Prospective Client Follow Up Marketing Mailer

This is a post card mailer used as a follow up touch point;providing information following contact via Connecto or other introductory touch. Its a key piece in the solicitation strategy to stir interest in using Harbor Loss Partners. As a follow up piece it needs to provide the salient selling points as to why use, choose or select Harbor to handle claims.
This should draw the reader's/receiver's eye to the key points and establish I their mind why they should choose to use Harbor Loss Partners for handling their property claims. Why they should place Harbor Loss Partners on their carrier's roster fro claim assignments.
Updates

Target Market(s)

These cards are sent to vendor managers at insurance companies or staff adjuster that hand out claim assignments.

Industry/Entity Type

Insurance

Requirements
Must have
• Professional look, fresh graphics/art work with salient selling points listed. Clean look. Clear and concise.
• Contact information.
Should not have
• clutter, too much written information.

```html
<!DOCTYPE html>
<html lang="en">
<head>
<meta charset="utf-8">
<title>Harbor Loss Partners – Follow Up Mailer</title>
<link href="https://fonts.googleapis.com/css2?family=Roboto+Condensed:wght@400;700&family=Open+Sans:wght@400;600&display=swap" rel="stylesheet">
<style>
  :root{
    --navy:#0d5aa7;
    --sky:#0e8ecf;
    --ink:#1f1f1f;
    --deep:#163a6b;
    --charcoal:#333436;
    --footer:#6d6e71;
    --page:#ebe8e3;
    --white:#ffffff;
  }
  *{margin:0;padding:0;box-sizing:border-box;}
  html,body{width:1200px;height:1200px;overflow:hidden;}
  body{background:var(--page);position:relative;font-family:"Open Sans",sans-serif;color:var(--ink);}

  .card{position:absolute;left:225px;width:750px;height:542px;background:var(--white);overflow:hidden;box-shadow:0 2px 6px rgba(0,0,0,.18);}
  .card-front{top:59px;}
  .card-back{top:630px;}

  /* front */
  .team-photo{position:absolute;inset:0;background:linear-gradient(100deg,#f4f5f7 0%,#dfe2e6 25%,#9fa6ae 50%,#6c7079 70%,#b8bcc3 88%,#e6e7ea 100%);}
  .front-shapes{position:absolute;inset:0;width:750px;height:542px;}
  .brand-box{position:absolute;left:32px;top:27px;width:160px;height:78px;background:var(--sky);display:flex;flex-direction:column;justify-content:center;align-items:center;}
  .brand-name{font-family:"Roboto Condensed",sans-serif;font-weight:700;color:var(--white);font-size:22px;line-height:1.05;text-align:center;letter-spacing:.5px;}
  .headline{position:absolute;left:49px;top:332px;font-family:"Roboto Condensed",sans-serif;font-weight:700;line-height:1;}
  .headline .lead{font-size:44px;color:var(--charcoal);letter-spacing:.5px;display:block;}
  .headline .l2{font-size:24px;color:var(--charcoal);display:block;margin-top:4px;}
  .headline .l3{font-size:26px;color:var(--deep);display:block;margin-top:1px;}
  .headline .l4{font-size:30px;color:var(--ink);display:block;margin-top:4px;}
  .contact-row{position:absolute;left:49px;top:506px;display:flex;gap:20px;align-items:center;font-family:"Roboto Condensed",sans-serif;font-size:15px;color:var(--ink);}
  .contact-item{display:flex;align-items:center;gap:7px;}
  .icon{width:19px;height:19px;flex:none;}

  /* back */
  .back-panel{position:absolute;left:0;top:0;width:431px;height:542px;background:linear-gradient(90deg,#ffffff 0%,#f2f2f2 100%);}
  .back-bands{position:absolute;left:0;top:0;width:431px;height:78px;}
  .services{position:absolute;left:45px;top:65px;width:370px;}
  .services h2{font-family:"Roboto Condensed",sans-serif;font-weight:700;font-size:18px;color:var(--charcoal);margin-bottom:6px;}
  .service{position:relative;padding-left:27px;margin-bottom:11px;}
  .service .icon{position:absolute;left:0;top:1px;}
  .service h3{font-family:"Roboto Condensed",sans-serif;font-weight:400;font-size:16px;color:var(--navy);line-height:1.15;}
  .service p{font-size:12.6px;line-height:1.25;margin-top:3px;text-align:justify;}
  .back-footer{position:absolute;left:0;top:459px;width:431px;height:83px;background:var(--footer);color:var(--white);font-family:"Roboto Condensed",sans-serif;font-size:13.5px;line-height:1.2;}
  .back-footer .col-a{position:absolute;left:45px;top:12px;}
  .back-footer .col-b{position:absolute;left:280px;top:14px;}
  .foot-line{display:flex;gap:8px;align-items:flex-start;margin-bottom:3px;}
  .foot-line .icon{width:16px;height:16px;}
  .col-b .foot-line{margin-bottom:9px;}
</style>
</head>
<body>

<section class="card card-front">
  <div class="team-photo" role="img" aria-label="Photo of a smiling team of business professionals in suits"></div>
  <svg class="front-shapes" viewBox="0 0 874 632" preserveAspectRatio="none" aria-hidden="true">
    <polygon points="0,175 720,520 874,400 874,470 700,582 0,250" fill="#0e8ecf"/>
    <polygon points="0,250 700,582 660,632 0,632" fill="#ffffff"/>
    <polygon points="0,345 170,240 740,525 874,425 874,470 700,582 0,250" fill="#ffffff"/>
    <polygon points="0,400 0,632 660,632 700,582 250,390" fill="#ffffff"/>
    <polygon points="0,290 167,182 740,495 874,400 874,425 740,525 170,240 0,345" fill="#0d5aa7"/>
    <polygon points="655,632 874,470 874,632" fill="#333436"/>
    <polygon points="700,582 874,470 874,480 712,588" fill="#ffffff"/>
  </svg>
  <div class="brand-box"><span class="brand-name">HARBOR<br>LOSS PARTNERS</span></div>
  <h1 class="headline">
    <span class="lead">BUILDING</span>
    <span class="l2">trustworthy relationships</span>
    <span class="l3">by delivering peace of mind</span>
    <span class="l4">to our clients' insureds</span>
  </h1>
  <div class="contact-row">
    <span class="contact-item"><svg class="icon" viewBox="0 0 20 20"><circle cx="10" cy="10" r="10" fill="#0d5aa7"/><circle cx="10" cy="10" r="5.5" fill="none" stroke="#fff" stroke-width="1.3"/><path d="M4.5 10h11M10 4.5v11M6 7h8M6 13h8" stroke="#fff" stroke-width="1"/></svg>www.harborlosspartners.com</span>
    <span class="contact-item"><svg class="icon" viewBox="0 0 20 20"><circle cx="10" cy="10" r="10" fill="#0d5aa7"/><path d="M6.5 5l2 .2.8 2.6-1.3 1a6 6 0 0 0 3 3l1-1.3 2.6.8.2 2c-4.5.8-9-3.7-8.3-8.3z" fill="#fff"/></svg>(555) 014-2290</span>
    <span class="contact-item"><svg class="icon" viewBox="0 0 20 20"><circle cx="10" cy="10" r="10" fill="#0d5aa7"/><rect x="5.5" y="6" width="9" height="8.5" fill="#fff"/><rect x="7" y="8" width="6" height="2" fill="#0d5aa7"/></svg>(555) 014-7731</span>
  </div>
</section>

<section class="card card-back">
  <div class="back-panel">
    <svg class="back-bands" viewBox="0 0 503 90" preserveAspectRatio="none" aria-hidden="true">
      <polygon points="0,0 130,0 0,45" fill="#0e8ecf"/>
      <polygon points="150,0 503,0 503,52 0,30 0,25" fill="#0d5aa7"/>
      <polygon points="0,38 503,62 503,90 0,62" fill="#0e8ecf"/>
    </svg>
    <div class="services">
      <h2>SERVICES</h2>
      <div class="service">
        <svg class="icon" viewBox="0 0 20 20"><circle cx="10" cy="10" r="10" fill="#0d5aa7"/><path d="M4.5 10 10 5l5.5 5h-1.7v4.5H6.2V10z" fill="#fff"/></svg>
        <h3>Property Adjusting</h3>
        <p>Adjusting residential and commercial daily claims</p>
      </div>
      <div class="service">
        <svg class="icon" viewBox="0 0 20 20"><circle cx="10" cy="10" r="10" fill="#0d5aa7"/><circle cx="9" cy="9" r="3.3" fill="none" stroke="#fff" stroke-width="1.6"/><path d="M11.5 11.5 14.5 14.5" stroke="#fff" stroke-width="1.8"/></svg>
        <h3>Subrogation Investigations</h3>
        <p>Assessing whether injury or property damage caused by another individual or company</p>
      </div>
      <div class="service">
        <svg class="icon" viewBox="0 0 20 20"><circle cx="10" cy="10" r="10" fill="#0d5aa7"/><circle cx="9" cy="9" r="3.8" fill="#fff"/><path d="M11.8 11.8 15 15" stroke="#fff" stroke-width="2"/></svg>
        <h3>AOE/COE Investigations</h3>
        <p>Gathering all facts relevant to filing of a workers' compensation claim</p>
      </div>
      <div class="service">
        <svg class="icon" viewBox="0 0 20 20"><circle cx="10" cy="10" r="10" fill="#0d5aa7"/><path d="M4.5 8 13 6l1.5 3-8 2.5z" fill="#fff"/><path d="M10 10.5v3.5h-3" stroke="#fff" stroke-width="1.3" fill="none"/></svg>
        <h3>Surveillance</h3>
        <p>Obtaining video footage to assist in the mitigation of claim exposure</p>
      </div>
      <div class="service">
        <svg class="icon" viewBox="0 0 20 20"><circle cx="10" cy="10" r="10" fill="#0d5aa7"/><circle cx="10" cy="10" r="5.5" fill="none" stroke="#fff" stroke-width="1.2"/><circle cx="10" cy="9" r="1.8" fill="#fff"/><path d="M7 13.5a3 3 0 0 1 6 0z" fill="#fff"/></svg>
        <h3>Social Media</h3>
        <p>Using technology and data base research to determine relevant information on an injured worker</p>
      </div>
      <div class="service">
        <svg class="icon" viewBox="0 0 20 20"><circle cx="10" cy="10" r="10" fill="#0d5aa7"/><path d="M6 6l8 8M14 6l-8 8" stroke="#fff" stroke-width="1.5"/></svg>
        <h3>Lien Negotiation Services</h3>
        <p>Negotiating workers' compensation lien issues (California) to reduce loss cost exposure on a claim file</p>
      </div>
    </div>
    <div class="back-footer">
      <div class="col-a">
        <div class="foot-line"><svg class="icon" viewBox="0 0 20 20"><circle cx="10" cy="10" r="10" fill="#0d5aa7"/><circle cx="10" cy="10" r="5.5" fill="none" stroke="#fff" stroke-width="1.3"/><path d="M4.5 10h11M10 4.5v11" stroke="#fff" stroke-width="1"/></svg><span>2480 Larkspur Harbor Way<br>Suite 2, Alder Bay, CA. 90021</span></div>
        <div class="foot-line"><svg class="icon" viewBox="0 0 20 20"><circle cx="10" cy="10" r="10" fill="#0d5aa7"/><circle cx="10" cy="10" r="5.5" fill="none" stroke="#fff" stroke-width="1.3"/><path d="M4.5 10h11M10 4.5v11" stroke="#fff" stroke-width="1"/></svg><span>www.harborlosspartners.com</span></div>
      </div>
      <div class="col-b">
        <div class="foot-line"><svg class="icon" viewBox="0 0 20 20"><circle cx="10" cy="10" r="10" fill="#0d5aa7"/><path d="M6.5 5l2 .2.8 2.6-1.3 1a6 6 0 0 0 3 3l1-1.3 2.6.8.2 2c-4.5.8-9-3.7-8.3-8.3z" fill="#fff"/></svg><span>(555) 014-2290</span></div>
        <div class="foot-line"><svg class="icon" viewBox="0 0 20 20"><circle cx="10" cy="10" r="10" fill="#0d5aa7"/><rect x="5.5" y="6" width="9" height="8.5" fill="#fff"/><rect x="7" y="8" width="6" height="2" fill="#0d5aa7"/></svg><span>(555) 014-7731</span></div>
      </div>
    </div>
  </div>
</section>

</body>
</html>
```